Design of slide which will later be converted to video

We need slides which will be converted to a video format for web and social media marketing. We are attaching our concept draft as a start

All slides are provided as background only at this point, but if someone has a great idea for any of the other topics, feel free to provide that as well.

Using the attached slides (11-15), please re-create the slides in a more artistic and unified presentation, using stock images of the dog characters (no animation). The Professor must be a Basset hound with glasses; the other dog characters should be similar to the ones used in the slides. Voices and music will be added later. Any detail that can be added to make the video a seamless narrative is encouraged.
Original source files for pics here: tulvexcanine-my.sharepoint-example.com/:f:/p/rodney/Kq_T8WPLx4vHmRzaNcf-bYsDkVm7Xtgahwe3Lp19B4M0Qz?e=HUMBAR
Updates

We have updated our brief to include source files for our images. Many designers have asked for this. Please have a look!

Target Market(s)

Fresh Pet Food

Industry/Entity Type

Pet Food

Colors
EB3D1F
EC4F4E
F09395
F8D3D4
FCEDEE

Requirements
Must have
• We want to keep the picture of the basset hound with glasses. We can potentially use other pictures of the other dogs, but not necessary. All dogs must be real pictures, no animation! The chalkboard needs to be a chalkboard - do not change it to something else, but please feel free to improve its look. This improvement - to all of our graphics - is what we are looking for.
Nice to have
• The chalkboard text come in as being written in real time; the dog pictures selected can be changed as per the designder creative instincts. We are pretty committed to the Basset Hound playing Professor Wickersham, but we are always open to suggestion

```html
<!DOCTYPE html>
<html lang="en">
<head>
<meta charset="utf-8">
<title>Fresh Bowl Forward – Ask Professor Wickersham</title>
<link rel="stylesheet" href="https://fonts.googleapis.com/css2?family=Montserrat:wght@400;600&display=swap">
<style>
  :root {
    --brand-red: #a8221a;
    --ring-pink: #d9a3a1;
    --ring-faint: #ecd3d2;
    --paper: #ffffff;
    --coat-dark: #7a3d1e;
    --coat-mid: #b0653a;
    --coat-light: #e8d9cc;
  }
  * { margin: 0; padding: 0; box-sizing: border-box; }
  html, body {
    width: 1200px;
    height: 675px;
    overflow: hidden;
    background: var(--paper);
  }
  .slide {
    position: relative;
    width: 1200px;
    height: 675px;
    background: var(--paper);
    overflow: hidden;
  }
  .rings {
    position: absolute;
    inset: 0;
  }
  .series-banner {
    position: absolute;
    left: 323px;
    top: 46px;
    width: 554px;
    height: 112px;
    background: var(--brand-red);
    display: flex;
    align-items: center;
    justify-content: center;
  }
  .series-banner h2 {
    font-family: "Montserrat", sans-serif;
    font-weight: 600;
    font-size: 44px;
    color: var(--paper);
    line-height: 1;
    white-space: nowrap;
  }
  .episode-title {
    position: absolute;
    right: 572px;
    top: 318px;
    text-align: right;
    color: var(--brand-red);
    font-family: "Montserrat", sans-serif;
    line-height: 1;
    white-space: nowrap;
  }
  .episode-title .kicker {
    display: block;
    font-weight: 400;
    font-size: 66px;
    letter-spacing: -0.5px;
  }
  .episode-title .name {
    display: block;
    font-weight: 600;
    font-size: 86px;
    letter-spacing: -1px;
    margin-top: 4px;
  }
  .professor-photo {
    position: absolute;
    left: 778px;
    top: 247px;
    width: 260px;
    height: 378px;
    border-radius: 90px 90px 30px 30px;
    background: linear-gradient(180deg, var(--coat-mid) 0%, var(--coat-dark) 45%, var(--coat-light) 100%);
  }
</style>
</head>
<body>
<main class="slide">
  <svg class="rings" width="1200" height="675" viewBox="0 0 1200 675" aria-hidden="true">
    <circle cx="894" cy="400" r="340" fill="none" stroke="var(--ring-faint)" stroke-width="1"/>
    <circle cx="894" cy="400" r="271" fill="none" stroke="var(--ring-pink)" stroke-width="1.2"/>
    <circle cx="894" cy="400" r="201" fill="none" stroke="var(--ring-pink)" stroke-width="1.5"/>
    <circle cx="894" cy="400" r="186" fill="var(--brand-red)"/>
  </svg>

  <header class="series-banner">
    <h2>Fresh Bowl Forward</h2>
  </header>

  <h1 class="episode-title">
    <span class="kicker">Ask Professor</span>
    <span class="name">Wickersham</span>
  </h1>

  <div class="professor-photo" role="img" aria-label="Photo of a seated basset hound wearing round glasses, Professor Wickersham"></div>
</main>
</body>
</html>
```